Occupational Therapist does home accessibility for disabled folks; needs business card design

We need a business card for a company in Portland, Oregon that specializes in making homes accessible, comfortable, and functional for people who are disabled or aging who would like to stay in THEIR home. Our medical background as Occupational Therapists allows us to translate the functional needs of the person into the recommendations for the design of the home remodel.

Target Market(s)

Elderly, children of elderly
People with disabilities, families of people with disabilities

Industry/Entity Type

Business

Contact Information for Business Card

Company name: HomeWise
Name: Danielle Reyes Crawford, OTR/L, CAPS, ECHM
Occupational Therapist, Home Modification & Accessibility Specialist
website: www.homewiseforyears.com
email: homewiseforyears@nestmail.example
phone: (503)218-4057
CCB #: 487315

Font styles to use
Sans Serif

Requirements
Must have
• My logo
• Easy to read font with contrasting background
• Please list the Services offered: Occupational Therapy, Home safety & accessibility assessments, Home modification consulting, project management
Nice to have
• Friendly, welcoming feel
Should not have
• Dark colored background

```html
<!DOCTYPE html>
<html lang="en">
<head>
<meta charset="utf-8">
<title>HomeWise Business Card</title>
<link rel="stylesheet" href="https://fonts.googleapis.com/css2?family=Open+Sans:wght@400;600&display=swap">
<style>
  :root {
    --page-bg: #ffffff;
    --card-bg: #ffffff;
    --brand-orange: #cd7f2b;
    --fold-shadow: #8a8a8a;
    --edge-shadow: #6b3f12;
    --ink: #111111;
    --wordmark: #ffffff;
  }
  * { margin: 0; padding: 0; box-sizing: border-box; }
  html, body {
    width: 1200px; height: 1000px; overflow: hidden;
    background: var(--page-bg);
    font-family: "Open Sans", Arial, sans-serif;
  }
  .canvas { position: relative; width: 1200px; height: 1000px; }
  .card {
    position: absolute; left: 90px; top: 207px;
    width: 1020px; height: 583px;
    background: var(--card-bg);
    box-shadow: 0 2px 6px rgba(0,0,0,0.18);
  }
  .card-art { position: absolute; left: 0; top: 0; }
  .line {
    position: absolute; white-space: nowrap; line-height: 1;
  }
  .holder-name { right: 73px; top: 87px; font-size: 44px; color: var(--ink); }
  .credentials { right: 75px; top: 152px; font-size: 32px; color: var(--brand-orange); }
  .role { font-size: 32px; color: var(--ink); transform: translateX(-50%); }
  .role-primary { left: 612px; top: 236px; }
  .role-secondary { left: 597px; top: 281px; }
  .contact { right: 69px; font-size: 32px; color: var(--ink); }
  .contact-email { top: 363px; }
  .contact-phone { top: 408px; }
  .website { right: 60px; top: 514px; font-size: 32px; color: var(--brand-orange); }
  .wordmark {
    left: 24px; top: 531px; font-size: 33px; font-weight: 600;
    color: var(--wordmark);
  }
</style>
</head>
<body>
<div class="canvas">
  <div class="card">
    <svg class="card-art" width="1020" height="583" viewBox="0 0 1020 583" aria-hidden="true">
      <defs>
        <linearGradient id="fold-shade" x1="0" y1="0" x2="1" y2="0">
          <stop offset="0" stop-color="var(--fold-shadow)" stop-opacity="0.75"/>
          <stop offset="1" stop-color="var(--fold-shadow)" stop-opacity="0"/>
        </linearGradient>
        <linearGradient id="edge-shade" x1="0" y1="0" x2="1" y2="0">
          <stop offset="0" stop-color="var(--edge-shadow)" stop-opacity="0"/>
          <stop offset="1" stop-color="var(--edge-shadow)" stop-opacity="0.55"/>
        </linearGradient>
      </defs>
      <polygon class="fold-shadow" points="210,425 287,583 210,583" fill="url(#fold-shade)"/>
      <polygon class="brand-flap" points="0,0 210,425 210,583 0,583" fill="var(--brand-orange)"/>
      <polygon class="flap-edge" points="0,0 210,425 196,425 0,18" fill="url(#edge-shade)"/>
    </svg>
    <div class="line wordmark">HomeWise</div>
    <div class="line holder-name">Danielle Reyes Crawford</div>
    <div class="line credentials">OTR/L, CAPS, ECHM</div>
    <div class="line role role-primary">Occupational Therapist</div>
    <div class="line role role-secondary">Home Modification &amp; Accessibility Specialist</div>
    <div class="line contact contact-email">homewiseforyears@nestmail.example</div>
    <div class="line contact contact-phone">(503) 218 - 4057</div>
    <div class="line website">www.homewiseforyears.com</div>
  </div>
</div>
</body>
</html>
```